Design an Outstanding flyer for my company.

I need a flyer designed for our window tinting company based in Brisbane Queensland Australia. The flyer will be targeting Home tinting. We also do mobile car tinting. Something in regards to this could be incorporated into the flyer as well.
I want it to be 2 sided DL size. Black background.
It really needs to Pop, and be a real attention getter.
It needs to be easy to read.
I have provided a mock up with the info on it from our marketing company. It will need a spellcheck etc to make sure everything is correct.
Everything about it can be changed however you like.
I have also included the company logo.

Lets see what you've got!

Target Market(s)

Home Owners

Industry/Entity Type

Home Improvement

Font styles to use
Other font styles liked:
• Duan Penh

Requirements
Must have
• All the information on the mock up. Clear and easy to read.
• Must Stand Out!

```html
<!DOCTYPE html>
<html lang="en">
<head>
<meta charset="utf-8">
<title>Brightline Window Tinting – DL Flyer</title>
<link href="https://fonts.googleapis.com/css2?family=Cinzel:wght@400;700&display=swap" rel="stylesheet">
<style>
  :root {
    --stage: #a9a9a9;
    --black: #050505;
    --gold: #e8c928;
    --gold-deep: #b8931a;
    --gold-light: #fff08a;
    --white: #ffffff;
    --ink: #111111;
  }
  * { box-sizing: border-box; margin: 0; padding: 0; }
  html, body { width: 1200px; height: 1200px; overflow: hidden; }
  body { background: var(--stage); position: relative; font-family: "Cinzel", "Times New Roman", serif; }

  .panel { position: absolute; top: 46px; width: 540px; height: 1110px; background: var(--black); overflow: hidden; }
  .panel--front { left: 45px; }
  .panel--back { left: 626px; }
  .panel-art { position: absolute; inset: 0; width: 540px; height: 1110px; }

  /* front */
  .brand { position: absolute; top: 52px; left: 0; width: 540px; display: flex; align-items: center; justify-content: center; gap: 16px; }
  .brand-dot { width: 46px; height: 46px; border-radius: 50%; background: var(--gold); flex: none; }
  .brand-text { display: flex; flex-direction: column; align-items: flex-start; }
  .brand-name { color: var(--gold); font-size: 40px; font-weight: 700; letter-spacing: 1px; line-height: 1; }
  .brand-sub { color: var(--gold); font-size: 11px; letter-spacing: 9px; margin-top: 8px; }
  .uv-claim { position: absolute; top: 1030px; left: 0; width: 540px; text-align: center; color: var(--gold); font-size: 38px; letter-spacing: 2px; }
  .uv-claim strong { color: var(--white); font-weight: 400; }

  /* back */
  .reasons-list { position: absolute; left: 128px; top: 124px; transform: rotate(-13deg); transform-origin: 0 0; list-style: none; color: var(--white); font-size: 15px; line-height: 24.5px; white-space: nowrap; }
  .reasons-list li { display: flex; align-items: center; gap: 8px; }
  .tick { width: 13px; height: 13px; flex: none; }

  .privacy { position: absolute; left: 36px; top: 500px; transform: rotate(-14deg); transform-origin: 0 0; white-space: nowrap; }
  .privacy-title { color: var(--ink); font-size: 36px; font-weight: 700; line-height: 1.1; }
  .privacy-sub { color: var(--gold-deep); font-size: 17px; font-weight: 700; line-height: 20px; margin-top: 4px; }
  .privacy-list { list-style: none; color: var(--ink); font-size: 12.5px; line-height: 22px; margin-top: 2px; padding-left: 28px; }
  .privacy-list li { display: flex; align-items: center; gap: 10px; }
  .star { width: 11px; height: 11px; flex: none; }

  .contact { position: absolute; left: 0; top: 972px; width: 540px; text-align: center; color: var(--white); }
  .contact-call { font-size: 18.5px; line-height: 21px; letter-spacing: 0.5px; }
  .contact-phones { display: flex; justify-content: center; gap: 56px; margin-top: 14px; font-size: 18px; }
  .contact-phones span { display: inline-flex; align-items: center; gap: 8px; }
  .contact-phones svg { width: 12px; height: 16px; }
  .contact-web { margin-top: 10px; font-size: 18px; }
  .contact-web span { color: var(--gold); }
</style>
</head>
<body>

<section class="panel panel--front">
  <svg class="panel-art" viewBox="0 0 540 1110" aria-hidden="false">
    <defs>
      <linearGradient id="houseTone" x1="0" y1="0" x2="0" y2="1">
        <stop offset="0" stop-color="#4a6a94"/>
        <stop offset="0.45" stop-color="#5b5d63"/>
        <stop offset="0.6" stop-color="#8a6a3c"/>
        <stop offset="0.8" stop-color="#3a4356"/>
        <stop offset="1" stop-color="#2a3242"/>
      </linearGradient>
      <linearGradient id="goldFill" x1="0" y1="0" x2="1" y2="1">
        <stop offset="0" stop-color="#fff06a"/>
        <stop offset="0.5" stop-color="#e8c928"/>
        <stop offset="1" stop-color="#c09a16"/>
      </linearGradient>
    </defs>
    <g role="img" aria-label="Photo of a white two-storey home at dusk with warm glowing windows and a wet driveway">
      <polygon points="0,268 540,152 540,970 0,970" fill="url(#houseTone)"/>
    </g>
    <polygon points="0,258 540,140 540,152 0,270" fill="url(#goldFill)"/>
    <rect x="0" y="966" width="540" height="9" fill="url(#goldFill)"/>

    <polygon points="351,750 540,712 540,782 351,820" fill="url(#goldFill)"/>
    <polygon points="351,820 375,815 375,830" fill="#8a6d10"/>
    <polygon points="351,838 540,800 540,870 351,908" fill="url(#goldFill)"/>
    <polygon points="351,908 375,903 375,918" fill="#8a6d10"/>
    <polygon points="351,926 540,888 540,958 351,996" fill="url(#goldFill)"/>
    <polygon points="351,996 375,991 375,1006" fill="#8a6d10"/>

    <g font-family="Cinzel, serif" font-size="46" fill="#0a0a0a">
      <text x="378" y="804" transform="rotate(-11 378 804)">KEEP</text>
      <text x="376" y="892" transform="rotate(-11 376 892)">HEAT</text>
      <text x="392" y="980" transform="rotate(-11 392 980)">OUT</text>
    </g>
  </svg>

  <div class="brand">
    <span class="brand-dot"></span>
    <div class="brand-text">
      <span class="brand-name">BRIGHTLINE</span>
      <span class="brand-sub">WINDOW TINTING</span>
    </div>
  </div>

  <p class="uv-claim">BLOCK <strong>99.9%</strong> UV RAYS</p>
</section>

<section class="panel panel--back">
  <svg class="panel-art" viewBox="0 0 540 1110">
    <defs>
      <linearGradient id="goldFillB" x1="0" y1="0" x2="1" y2="1">
        <stop offset="0" stop-color="#fff06a"/>
        <stop offset="0.5" stop-color="#e8c928"/>
        <stop offset="1" stop-color="#c09a16"/>
      </linearGradient>
      <linearGradient id="paper" x1="0" y1="0" x2="1" y2="1">
        <stop offset="0" stop-color="#ffffff"/>
        <stop offset="0.6" stop-color="#f3f3f3"/>
        <stop offset="1" stop-color="#d8d8d8"/>
      </linearGradient>
      <linearGradient id="bathTone" x1="0" y1="0" x2="0" y2="1">
        <stop offset="0" stop-color="#c9b69c"/>
        <stop offset="0.55" stop-color="#d9cbb6"/>
        <stop offset="1" stop-color="#efeae2"/>
      </linearGradient>
    </defs>
    <polygon points="82,88 462,0 540,0 540,24 86,130" fill="url(#goldFillB)"/>
    <polygon points="150,115 172,110 172,128" fill="#7a600e"/>
    <text x="108" y="122" transform="rotate(-13 108 122)" font-family="Cinzel, serif" font-size="32" fill="#0a0a0a" textLength="250">KEEP HEAT OUT</text>
    <text x="82" y="448" transform="rotate(-90 82 448)" font-family="Cinzel, serif" font-size="50" fill="#e8c928" textLength="292">REASONS</text>

    <polygon points="0,484 540,376 540,699 0,811" fill="url(#paper)"/>
    <polygon points="0,474 540,366 540,378 0,486" fill="url(#goldFillB)"/>
    <g role="img" aria-label="Photo of a white bathtub beneath a tinted bathroom window">
      <polygon points="0,811 540,699 540,942 0,942" fill="url(#bathTone)"/>
    </g>
    <rect x="0" y="942" width="540" height="9" fill="url(#goldFillB)"/>
  </svg>

  <ul class="reasons-list">
    <li><svg class="tick" viewBox="0 0 13 13"><rect x="1" y="3" width="9" height="9" fill="none" stroke="#e8c928" stroke-width="1.4"/><path d="M3 7l2.5 2.5L12 1.5" fill="none" stroke="#e8c928" stroke-width="2"/></svg>REDUCE GLARE.</li>
    <li><svg class="tick" viewBox="0 0 13 13"><rect x="1" y="3" width="9" height="9" fill="none" stroke="#e8c928" stroke-width="1.4"/><path d="M3 7l2.5 2.5L12 1.5" fill="none" stroke="#e8c928" stroke-width="2"/></svg>REDUCE ENERGY COSTS.</li>
    <li><svg class="tick" viewBox="0 0 13 13"><rect x="1" y="3" width="9" height="9" fill="none" stroke="#e8c928" stroke-width="1.4"/><path d="M3 7l2.5 2.5L12 1.5" fill="none" stroke="#e8c928" stroke-width="2"/></svg>CONTROL THE AMOUNT OF LIGHT</li>
    <li><svg class="tick" viewBox="0 0 13 13"><rect x="1" y="3" width="9" height="9" fill="none" stroke="#e8c928" stroke-width="1.4"/><path d="M3 7l2.5 2.5L12 1.5" fill="none" stroke="#e8c928" stroke-width="2"/></svg>ENTERING YOUR HOME.</li>
    <li><svg class="tick" viewBox="0 0 13 13"><rect x="1" y="3" width="9" height="9" fill="none" stroke="#e8c928" stroke-width="1.4"/><path d="M3 7l2.5 2.5L12 1.5" fill="none" stroke="#e8c928" stroke-width="2"/></svg>REDUCE CARBON FOOTPRINT.</li>
    <li><svg class="tick" viewBox="0 0 13 13"><rect x="1" y="3" width="9" height="9" fill="none" stroke="#e8c928" stroke-width="1.4"/><path d="M3 7l2.5 2.5L12 1.5" fill="none" stroke="#e8c928" stroke-width="2"/></svg>MAKE HOME MORE BEAUTIFUL.</li>
    <li><svg class="tick" viewBox="0 0 13 13"><rect x="1" y="3" width="9" height="9" fill="none" stroke="#e8c928" stroke-width="1.4"/><path d="M3 7l2.5 2.5L12 1.5" fill="none" stroke="#e8c928" stroke-width="2"/></svg>ELIMINATE HOME HOT SPOTS.</li>
    <li><svg class="tick" viewBox="0 0 13 13"><rect x="1" y="3" width="9" height="9" fill="none" stroke="#e8c928" stroke-width="1.4"/><path d="M3 7l2.5 2.5L12 1.5" fill="none" stroke="#e8c928" stroke-width="2"/></svg>PROTECT AGAINST BROKEN GLASS.</li>
    <li><svg class="tick" viewBox="0 0 13 13"><rect x="1" y="3" width="9" height="9" fill="none" stroke="#e8c928" stroke-width="1.4"/><path d="M3 7l2.5 2.5L12 1.5" fill="none" stroke="#e8c928" stroke-width="2"/></svg>REGULATE ENERGY.</li>
    <li><svg class="tick" viewBox="0 0 13 13"><rect x="1" y="3" width="9" height="9" fill="none" stroke="#e8c928" stroke-width="1.4"/><path d="M3 7l2.5 2.5L12 1.5" fill="none" stroke="#e8c928" stroke-width="2"/></svg>PROTECTS UPHOLSTERY.</li>
  </ul>

  <div class="privacy">
    <h2 class="privacy-title">INCREASE PRIVACY</h2>
    <p class="privacy-sub">20 REASONS WHY HOME WINDOW TINTING<br>IS PERFECT FOR YOU.</p>
    <ul class="privacy-list">
      <li><svg class="star" viewBox="0 0 10 10"><path d="M5 0l1.2 3.6H10L6.9 5.8 8.1 9.5 5 7.2 1.9 9.5 3.1 5.8 0 3.6h3.8z" fill="#b8931a"/></svg>IMPROVE EFFECTIVENESS OF ROOF INSULATION.</li>
      <li><svg class="star" viewBox="0 0 10 10"><path d="M5 0l1.2 3.6H10L6.9 5.8 8.1 9.5 5 7.2 1.9 9.5 3.1 5.8 0 3.6h3.8z" fill="#b8931a"/></svg>IMPROVE HEALTH.</li>
      <li><svg class="star" viewBox="0 0 10 10"><path d="M5 0l1.2 3.6H10L6.9 5.8 8.1 9.5 5 7.2 1.9 9.5 3.1 5.8 0 3.6h3.8z" fill="#b8931a"/></svg>REDUCES INTERIOR FLOOR FADING.</li>
      <li><svg class="star" viewBox="0 0 10 10"><path d="M5 0l1.2 3.6H10L6.9 5.8 8.1 9.5 5 7.2 1.9 9.5 3.1 5.8 0 3.6h3.8z" fill="#b8931a"/></svg>ELIMINATE NEED FOR BLINDS.</li>
      <li><svg class="star" viewBox="0 0 10 10"><path d="M5 0l1.2 3.6H10L6.9 5.8 8.1 9.5 5 7.2 1.9 9.5 3.1 5.8 0 3.6h3.8z" fill="#b8931a"/></svg>STRENGTHEN YOUR WINDOWS.</li>
      <li><svg class="star" viewBox="0 0 10 10"><path d="M5 0l1.2 3.6H10L6.9 5.8 8.1 9.5 5 7.2 1.9 9.5 3.1 5.8 0 3.6h3.8z" fill="#b8931a"/></svg>INSULATE IN WINTER.</li>
      <li><svg class="star" viewBox="0 0 10 10"><path d="M5 0l1.2 3.6H10L6.9 5.8 8.1 9.5 5 7.2 1.9 9.5 3.1 5.8 0 3.6h3.8z" fill="#b8931a"/></svg>AFFORDABLE.</li>
    </ul>
  </div>

  <div class="contact">
    <p class="contact-call">CALL BRISBANE’S LEADER IN HOME WINDOW<br>TINTING NOW.</p>
    <p class="contact-phones">
      <span><svg viewBox="0 0 12 16"><path d="M3 1l2 3-1.5 1.5c.5 2 2 4.5 3.5 5.5L8.5 9.5l2.5 2.5-2 3C5 14 1 8 1 3z" fill="#e8c928"/></svg>07 3000 0142</span>
      <span><svg viewBox="0 0 12 16"><rect x="2" y="1" width="8" height="14" rx="1.5" fill="none" stroke="#e8c928" stroke-width="1.6"/><rect x="4" y="3.5" width="4" height="5" fill="#e8c928"/></svg>0400 000 318</span>
    </p>
    <p class="contact-web">www.<span>BRIGHTLINETINTING</span>.com.au</p>
  </div>
</section>

</body>
</html>
```